Would like a Northwest feel to the look, something NOT typical of what you would see on a typical Home Inspectors logo. Real estate cards all the same as well, and would like to stand out. Earthy, green, Northwest. Sadly a portrait seems to be a requirement (see the attached). I inspect residential homes for buyers and sellers.

Target Market(s)

Home Buyers and Sellers

Industry/Entity Type

Home Inspection

Contact Information for Business Card

See description
Note: The name Corvaneth is a Chinook word that means 'Friend'. Please do not associate the name with the Whale that shows up on 99% of google searches.

Logo Text

Corvaneth Home Inspections

Colors

Designer to choose colors to be used in the design.

Requirements
Must have
• Phone Num: 541-672-8153
• Address: 732 SW 219th Av Num 618
• Portland, Oregon 97388
• Email: glen@corvanethhomeinspection.example
• Website: www.CorvanethHomeInspection.example
• Additional Note: Need to add the Obravex logo (icon). It should be small and not the focus of the card. The logo can be found at Obravex.example
Nice to have
• I am open
Should not have
• Cant think of anything

```html
<!DOCTYPE html>
<html lang="en">
<head>
<meta charset="utf-8">
<title>Corvaneth Home Inspections – Business Card</title>
<link href="https://fonts.googleapis.com/css2?family=Lato:wght@400;700&display=swap" rel="stylesheet">
<style>
  :root {
    --forest: #2b4422;
    --forest-deep: #263d1f;
    --lime: #a5bf32;
    --leaf: #7fae38;
    --white: #ffffff;
    --page: #ffffff;
  }
  * { margin: 0; padding: 0; box-sizing: border-box; }
  html, body { width: 1200px; height: 1200px; overflow: hidden; background: var(--page); }
  body { position: relative; font-family: 'Lato', sans-serif; }

  .card { position: absolute; left: 120px; width: 960px; height: 549px; overflow: hidden; }
  .card-front { top: 34px; background: var(--forest); }
  .card-back { top: 617px; background: var(--forest-deep); }

  .portrait {
    position: absolute; left: 70px; top: 34px; width: 246px; height: 332px;
    background: radial-gradient(ellipse at 45% 55%, #b98d6e 0%, #8a6a55 35%, #6b4a2a 65%, #c7801f 100%);
  }
  .accent-band {
    position: absolute; left: 361px; top: 0; width: 69px; height: 454px;
    background: var(--lime); border-radius: 0 0 35px 35px;
  }

  .brand { position: absolute; display: flex; align-items: center; color: var(--leaf); font-weight: 700; }
  .brand-mark { border-radius: 50%; background: var(--leaf); flex: none; }
  .brand-front { left: 58px; top: 398px; width: 280px; gap: 14px; font-size: 26px; line-height: 1.1; }
  .brand-front .brand-mark { width: 62px; height: 62px; }
  .brand-back { left: 220px; top: 170px; width: 560px; gap: 30px; font-size: 54px; line-height: 1.08; }
  .brand-back .brand-mark { width: 150px; height: 150px; }

  .person { position: absolute; left: 527px; top: 26px; }
  .person-name { color: var(--white); font-size: 52px; font-weight: 400; line-height: 1.1; }
  .person-role { color: var(--lime); font-size: 21px; margin-top: 4px; }

  .contact-list { position: absolute; left: 448px; top: 128px; list-style: none; }
  .contact-item { display: flex; align-items: center; height: 62px; margin-bottom: 22px; color: var(--white); font-size: 20px; letter-spacing: 0.3px; }
  .contact-icon { width: 62px; height: 62px; border-radius: 50%; background: var(--white); display: flex; align-items: center; justify-content: center; margin-right: 18px; flex: none; }
  .contact-icon svg { width: 36px; height: 36px; }

  .address { position: absolute; left: 482px; top: 416px; color: var(--white); font-size: 22px; line-height: 1.3; }

  .web-band {
    position: absolute; left: 0; bottom: 0; width: 100%; height: 70px;
    background: var(--lime); color: var(--forest); font-size: 22px; letter-spacing: 0.4px;
    display: flex; align-items: center; justify-content: center;
  }
</style>
</head>
<body>

<section class="card card-front">
  <div class="portrait" role="img" aria-label="Portrait photo of the home inspector"></div>
  <div class="accent-band"></div>

  <div class="brand brand-front">
    <span class="brand-mark"></span>
    <span class="brand-name">Corvaneth Home Inspections</span>
  </div>

  <div class="person">
    <h1 class="person-name">Glen</h1>
    <p class="person-role">Home inspector</p>
  </div>

  <ul class="contact-list">
    <li class="contact-item">
      <span class="contact-icon">
        <svg viewBox="0 0 24 24" aria-hidden="true"><path fill="#7fae38" d="M6.6 10.8a15.1 15.1 0 0 0 6.6 6.6l2.2-2.2a1 1 0 0 1 1-.25 11.4 11.4 0 0 0 3.6.57 1 1 0 0 1 1 1V20a1 1 0 0 1-1 1A17 17 0 0 1 3 4a1 1 0 0 1 1-1h3.5a1 1 0 0 1 1 1c0 1.25.2 2.45.57 3.57a1 1 0 0 1-.25 1z"/></svg>
      </span>
      <span>541-672-8153</span>
    </li>
    <li class="contact-item">
      <span class="contact-icon">
        <svg viewBox="0 0 24 24" aria-hidden="true" fill="none" stroke="#7fae38" stroke-width="1.4" stroke-linejoin="round"><path d="M3 10l9-6 9 6v10H3z"/><path d="M3 10l9 6 9-6M3 20l7-5.5M21 20l-7-5.5"/></svg>
      </span>
      <span>glen@corvanethhomeinspection.example</span>
    </li>
    <li class="contact-item">
      <span class="contact-icon">
        <svg viewBox="0 0 24 24" aria-hidden="true" fill="none" stroke="#7fae38" stroke-width="1.5"><circle cx="12" cy="12" r="9"/><ellipse cx="12" cy="12" rx="4" ry="9"/><path d="M3 12h18M4.5 7.5h15M4.5 16.5h15"/></svg>
      </span>
      <span>www.CorvanethHomeInspection.example</span>
    </li>
  </ul>

  <p class="address">732 SW 219th Av Num 618<br>Portland, Oregon 97388</p>
</section>

<section class="card card-back">
  <div class="brand brand-back">
    <span class="brand-mark"></span>
    <span class="brand-name">Corvaneth Home Inspections</span>
  </div>
  <div class="web-band">www.CorvanethHomeInspection.example</div>
</section>

</body>
</html>
```